Home Improvement Company in need of a "Banner & Billboard Design"

I'm Looking for a Banner design 4X6 With Company Logo, Phone Number, website, Credentials and services.. I picture a charcoal/matte background i also want to look like a house shape design i will upload the sample...

I'm looking for a Billboard design to target homeowners who need Roofing Services. I need logo, number, website, KTL, Credentials and a catchy title. i will like to use the same colors for branding

Target Market(s)

Homeowners, Investors,

Industry/Entity Type

Home Improvement

Font styles to use
Decorative

Colors
00a990
5c5c5c
333333

Requirements
Must have
• All Credentials, Phone number, website, logo, logo colors, services, Eye Catchy, Direct Message, Friendly feeling,
• (614) 372 - 9058
• Roofing Gutters Painting Pressure Washing Exterior Design
Nice to have
• A catchy title, A direct message to a homeowner looking for home improvement services. noticeable
Should not have
• not Busy, no

```html
<!DOCTYPE html>
<html lang="en">
<head>
<meta charset="utf-8">
<title>Ridgeline Home Exteriors – Banner</title>
<link href="https://fonts.googleapis.com/css2?family=Oswald:wght@500&family=Open+Sans:wght@700&display=swap" rel="stylesheet">
<style>
  :root {
    --teal: #00a990;
    --teal-band: #1f9a86;
    --charcoal: #333333;
    --panel: #3a3a3a;
    --gray: #5c5c5c;
    --icon: #4a4a4a;
    --white: #ffffff;
    --page: #ffffff;
    --badge-red: #8a1f1f;
    --badge-navy: #1f2a5c;
  }
  * { margin: 0; padding: 0; box-sizing: border-box; }
  html, body { width: 965px; height: 1200px; overflow: hidden; background: var(--page); }
  .banner {
    position: absolute; left: 30px; top: 300px;
    width: 905px; height: 600px;
    background: var(--panel);
    overflow: hidden;
  }
  .brand {
    position: absolute; left: 50px; top: 95px; width: 240px;
    font-family: 'Oswald', sans-serif; font-weight: 500;
    color: var(--teal); text-transform: uppercase;
    font-size: 34px; line-height: 1.05; letter-spacing: 1px;
  }
  .brand-mark {
    display: block; width: 28px; height: 28px; background: var(--teal);
    margin-bottom: 14px;
  }
  .services {
    position: absolute; top: 70px;
    list-style: none;
    font-family: 'Oswald', sans-serif; font-weight: 500;
    font-size: 25px; color: var(--white);
  }
  .services li { height: 40px; display: flex; align-items: center; }
  .services li::before {
    content: ""; width: 12px; height: 12px; background: var(--teal);
    margin-right: 22px; flex: none;
  }
  .services--left { left: 345px; }
  .services--right { left: 600px; }
  .phone {
    position: absolute; left: 50px; top: 335px;
    font-family: 'Open Sans', sans-serif; font-weight: 700;
    font-size: 60px; color: var(--white); letter-spacing: 0.5px;
  }
  .website {
    position: absolute; left: 55px; top: 422px;
    font-family: 'Open Sans', sans-serif; font-weight: 700;
    font-size: 29px; color: var(--teal);
  }
  .badge { position: absolute; border-radius: 4px; }
  .badge--cert { left: 600px; top: 418px; width: 165px; height: 62px; background: var(--badge-red); }
  .badge--listing { left: 782px; top: 365px; width: 75px; height: 117px; background: var(--badge-navy); border: 2px solid #5a6aa8; }
  .footer { position: absolute; left: 0; bottom: 0; }
</style>
</head>
<body>
  <section class="banner">
    <div class="brand"><span class="brand-mark"></span>Ridgeline Home Exteriors</div>

    <ul class="services services--left">
      <li>Roof Cleaning</li>
      <li>Moss Treatment</li>
      <li>Repairs Overview</li>
      <li>Gutters Overview</li>
    </ul>
    <ul class="services services--right">
      <li>Attic Ventilation</li>
      <li>Skylights</li>
      <li>Pressure Washing</li>
      <li>Paiting Overview</li>
    </ul>

    <div class="phone">(614) 372 - 9058</div>
    <div class="website">www.RidgelineExteriors.com</div>

    <div class="badge badge--cert" aria-label="Certification badge"></div>
    <div class="badge badge--listing" aria-label="Business listing badge"></div>

    <svg class="footer" width="905" height="110" viewBox="0 0 905 110">
      <polygon points="0,33 465,33 445,110 0,110" fill="var(--gray)"/>
      <polygon points="490,0 905,0 905,110 458,110" fill="var(--teal-band)"/>
      <g fill="none" stroke="var(--icon)" stroke-width="3" stroke-linecap="round">
        <!-- phone handset -->
        <path d="M170 61 q-4 4 0 12 q6 10 16 16 q8 4 12 0 l-6 -7 l-5 3 q-7 -4 -10 -10 l3 -5 z"/>
        <!-- globe -->
        <circle cx="220" cy="73" r="12"/>
        <ellipse cx="220" cy="73" rx="5" ry="12"/>
        <line x1="208" y1="73" x2="232" y2="73"/>
        <!-- envelope -->
        <rect x="250" y="63" width="26" height="19"/>
        <polyline points="250,63 263,74 276,63"/>
      </g>
    </svg>
  </section>
</body>
</html>
```